Brightpath Dentistry - Flyer - Modern & Eye catching campaign flyer

Need front & back side full page flyer designs for both 1) Grand opening 2) On-going campaign.

Attached the new dental office logo.
Attached our other dental clinic flyer designs for content.

Target Market(s)

Cosmetic dentistry

Industry/Entity Type

Health Care

Requirements
Must have
• decent, modern and eye catching marketing flyers.
Nice to have
• - Nice space
• - Highlight phone number
• - Highlight special features like convenient hours, call or text, for all ages, digital facility, etc
Should not have
• - Don't want to fill the flyer with too much wordings
• - Too many colors

```html
<!DOCTYPE html>
<html lang="en">
<head>
<meta charset="utf-8">
<title>Brightpath Dentistry – Grand Opening Flyer</title>
<link rel="stylesheet" href="https://fonts.googleapis.com/css2?family=Archivo+Black&family=Lato:wght@700;900&family=Open+Sans:wght@700&family=Questrial&family=Tinos:wght@400;700&display=swap">
<style>
  :root {
    --navy: #1c5aa6;
    --navy-deep: #174f96;
    --green: #2e8b33;
    --sky: #6ccbe8;
    --sky-wash: #e2f2fa;
    --white: #ffffff;
    --ink: #111111;
    --stage: #eceff2;
  }
  * { box-sizing: border-box; margin: 0; padding: 0; }
  html, body { width: 1200px; height: 1200px; overflow: hidden; background: var(--stage); }
  .canvas { position: relative; width: 1200px; height: 1200px; }
  .flyer {
    position: absolute; left: 207px; top: 43px;
    width: 604px; height: 856px;
    transform: scale(1.3); transform-origin: 0 0;
    background: var(--sky-wash); overflow: hidden;
    box-shadow: 0 2px 6px rgba(0,0,0,.15);
  }
  .header-wave { position: absolute; left: 0; top: 0; width: 604px; height: 280px; }
  .brand { position: absolute; left: 44px; top: 36px; display: flex; align-items: center; gap: 10px; }
  .brand-dot { width: 26px; height: 26px; border-radius: 50%; background: var(--navy); }
  .brand-name { font-family: "Lato", sans-serif; font-weight: 900; font-size: 27px; color: var(--navy); letter-spacing: -.2px; }
  .tagline { position: absolute; left: 138px; top: 73px; font-family: "Lato", sans-serif; font-weight: 700; font-size: 16px; color: var(--green); }
  .web { position: absolute; left: 438px; top: 50px; display: flex; align-items: center; gap: 4px; font-family: "Tinos", serif; font-weight: 700; font-size: 11px; color: var(--navy); }
  .phone-pill {
    position: absolute; left: 113px; top: 118px; width: 260px; height: 40px;
    border-radius: 20px; background: var(--sky);
    display: flex; align-items: center; justify-content: center; gap: 10px;
    font-family: "Tinos", serif; font-size: 28px; color: var(--white);
  }
  .photo { position: absolute; border-radius: 50%; border: 6px solid var(--white); }
  .photo-hero { left: 368px; top: 85px; width: 264px; height: 264px;
    background: radial-gradient(circle at 45% 45%, #f3d9c6 0%, #e8c9a6 45%, #d9b878 75%, #c9a46a 100%); }
  .photo-exam { left: 44px; top: 369px; width: 168px; height: 168px; border-width: 5px;
    box-shadow: 0 0 0 2px #cfe6f3;
    background: radial-gradient(circle at 55% 45%, #efd3c2 0%, #cfa58e 50%, #8a5c45 100%); }
  .headline { position: absolute; left: 55px; top: 244px; font-family: "Archivo Black", sans-serif; font-size: 53px; line-height: 48px; color: var(--navy); letter-spacing: .5px; }
  .offers-title {
    position: absolute; left: 282px; top: 368px; width: 280px; height: 48px;
    background: var(--white); border-radius: 8px;
    font-family: "Lato", sans-serif; font-weight: 700; font-size: 28px; color: var(--green);
    display: flex; align-items: center; justify-content: center;
  }
  .offers { position: absolute; right: 41px; top: 425px; list-style: none; }
  .offers li { display: flex; align-items: center; justify-content: flex-start; gap: 6px; height: 32px; font-family: "Questrial", sans-serif; font-weight: 700; font-size: 19.5px; color: var(--ink); -webkit-text-stroke: .3px var(--ink); }
  .offers li:first-child { font-family: "Tinos", serif; -webkit-text-stroke: 0; }
  .offers li.o1 { margin-left: 27px; }
  .offers li.o3 { margin-left: 32px; }
  .services-title { position: absolute; left: 0; width: 604px; top: 545px; text-align: center; font-family: "Lato", sans-serif; font-weight: 900; font-size: 21px; color: var(--green); }
  .services { position: absolute; left: 75px; top: 576px; width: 459px; height: 142px; background: var(--navy); border-radius: 18px; }
  .service { position: absolute; width: 96px; margin-left: -48px; text-align: center; color: var(--white); font-family: "Open Sans", sans-serif; font-weight: 700; font-size: 8.5px; line-height: 10px; text-transform: uppercase; }
  .service svg { display: block; margin: 0 auto 4px; width: 22px; height: 24px; }
  .service .note { text-transform: none; }
  .terms { position: absolute; left: 0; width: 604px; top: 738px; text-align: center; font-family: "Tinos", serif; font-size: 14.5px; color: var(--ink); }
  .welcome { position: absolute; left: 0; width: 604px; top: 760px; text-align: center; font-family: "Open Sans", sans-serif; font-weight: 700; font-size: 14.5px; color: var(--ink); }
  .hours-band { position: absolute; left: 0; top: 790px; width: 604px; height: 46px; }
  .hours-text { position: absolute; left: 0; width: 604px; top: 810px; text-align: center; font-family: "Tinos", serif; font-weight: 700; font-size: 16px; color: var(--white); letter-spacing: .3px; }
</style>
</head>
<body>
<div class="canvas">
  <article class="flyer">
    <svg class="header-wave" viewBox="0 0 604 280" aria-hidden="true">
      <path d="M0 0 H604 V252 C470 244 220 190 0 118 Z" fill="#ffffff"/>
      <path d="M0 118 C220 190 470 244 604 252 V266 C460 262 210 205 0 126 Z" fill="#1c5aa6"/>
    </svg>

    <div class="brand">
      <span class="brand-dot"></span>
      <span class="brand-name">Brightpath Dentistry</span>
    </div>
    <p class="tagline">Modern Dental Care for All Ages</p>
    <p class="web">
      <svg width="11" height="11" viewBox="0 0 12 12" aria-hidden="true"><circle cx="6" cy="6" r="5" fill="none" stroke="#1c5aa6" stroke-width="1.3"/><path d="M1 6 H11 M6 1 C3 4 3 8 6 11 M6 1 C9 4 9 8 6 11" fill="none" stroke="#1c5aa6" stroke-width="1"/></svg>
      www.BrightpathDental.com
    </p>

    <div class="phone-pill">
      <svg width="20" height="22" viewBox="0 0 20 22" aria-hidden="true"><ellipse cx="10" cy="11" rx="9" ry="10" fill="none" stroke="#fff" stroke-width="1.6"/><path d="M7 6 C5 9 6 14 10 17 L12 15 L10 13 C9 12 8.5 10 9 9 L11 8 Z" fill="#fff"/></svg>
      <span>555.014.2280</span>
    </div>

    <div class="photo photo-hero" role="img" aria-label="Photo of a smiling young woman with long blonde hair resting her chin on her hands"></div>

    <h1 class="headline">GRAND<br>OPENING !</h1>

    <div class="photo photo-exam" role="img" aria-label="Photo of a patient smiling during a dental check-up with instruments"></div>

    <div class="offers-title">Special offers:</div>
    <ul class="offers">
      <li class="o1"><svg width="18" height="18" viewBox="0 0 18 18" aria-hidden="true"><path d="M2 10 L7 15 L16 2" fill="none" stroke="#2e8b33" stroke-width="2.2"/></svg>Free Kids Dental Screening</li>
      <li class="o2"><svg width="18" height="18" viewBox="0 0 18 18" aria-hidden="true"><path d="M2 10 L7 15 L16 2" fill="none" stroke="#2e8b33" stroke-width="2.2"/></svg>$25 Adults Dental Screening</li>
      <li class="o3"><svg width="18" height="18" viewBox="0 0 18 18" aria-hidden="true"><path d="M2 10 L7 15 L16 2" fill="none" stroke="#2e8b33" stroke-width="2.2"/></svg>15% off on Treatment Plan</li>
    </ul>

    <h2 class="services-title">Our Services :</h2>
    <section class="services">
      <div class="service" style="left:77px; top:10px">
        <svg viewBox="0 0 22 24" aria-hidden="true"><path d="M4 3 C7 1 9 3 11 3 C13 3 15 1 18 3 C21 6 19 11 17 14 L16 22 L13 16 L11 15 L9 16 L6 22 L5 14 C3 11 1 6 4 3 Z" fill="none" stroke="#fff" stroke-width="1.6"/><path d="M11 6 V13" stroke="#fff" stroke-width="1.4"/></svg>
        Root Canal<br>Therapy
      </div>
      <div class="service" style="left:175px; top:14px">
        <svg viewBox="0 0 22 24" aria-hidden="true"><path d="M2 8 C2 4 20 4 20 8 V14 H2 Z" fill="#fff"/><path d="M5 8 V13 M9 8 V13 M13 8 V13 M17 8 V13" stroke="#1c5aa6" stroke-width="1.3"/></svg>
        Dentures
      </div>
      <div class="service" style="left:275px; top:10px">
        <svg viewBox="0 0 22 24" aria-hidden="true"><path d="M5 2 C8 1 14 1 17 2 C18 5 16 8 11 8 C6 8 4 5 5 2 Z" fill="#fff"/><path d="M7 10 H15 M7 13 H15 M8 16 H14 M9 19 H13" stroke="#fff" stroke-width="1.6"/></svg>
        Implants
      </div>
      <div class="service" style="left:382px; top:10px">
        <svg viewBox="0 0 22 24" aria-hidden="true"><rect x="1" y="6" width="20" height="10" rx="3" fill="none" stroke="#fff" stroke-width="1.5"/><path d="M1 11 H21 M6 6 V16 M11 6 V16 M16 6 V16" stroke="#fff" stroke-width="1.2"/></svg>
        ClearAlign<br><span class="note">(Invisible braces)</span>
      </div>
      <div class="service" style="left:53px; top:73px">
        <svg viewBox="0 0 22 24" aria-hidden="true"><path d="M5 6 C8 4 9 6 11 6 C13 6 14 4 17 6 C19 9 17 13 16 16 L15 22 L12 17 H10 L7 22 L6 16 C5 13 3 9 5 6 Z" fill="#fff"/><path d="M3 2 L5 4 M11 0 V2 M19 2 L17 4" stroke="#fff" stroke-width="1.2"/></svg>
        Glow Teeth<br>Whitening
      </div>
      <div class="service" style="left:151px; top:73px">
        <svg viewBox="0 0 22 24" aria-hidden="true"><path d="M2 14 C4 20 18 20 20 14" fill="none" stroke="#fff" stroke-width="2"/><path d="M7 4 C9 3 10 4 11 4 C12 4 13 3 15 4 C16 7 15 10 14 12 L13 16 H9 L8 12 C7 10 6 7 7 4 Z" fill="#fff"/></svg>
        Extractions
      </div>
      <div class="service" style="left:243px; top:73px">
        <svg viewBox="0 0 22 24" aria-hidden="true"><path d="M3 8 C3 3 19 3 19 8 C19 12 16 15 11 15 C6 15 3 12 3 8 Z" fill="none" stroke="#fff" stroke-width="1.5"/><path d="M6 7 V12 M9 6 V13 M13 6 V13 M16 7 V12" stroke="#fff" stroke-width="1.1"/><path d="M5 17 C8 21 14 21 17 17" fill="none" stroke="#fff" stroke-width="1.5"/></svg>
        Veneers
      </div>
      <div class="service" style="left:325px; top:73px">
        <svg viewBox="0 0 22 24" aria-hidden="true"><rect x="2" y="7" width="18" height="9" rx="4" fill="none" stroke="#fff" stroke-width="1.5"/><path d="M5 9 V14 M8 9 V14 M11 9 V14 M14 9 V14 M17 9 V14" stroke="#fff" stroke-width="1"/></svg>
        Night Guards
      </div>
      <div class="service" style="left:414px; top:73px">
        <svg viewBox="0 0 22 24" aria-hidden="true"><path d="M5 3 C8 1 9 3 11 3 C13 3 14 1 17 3 C19 6 18 9 17 11 H5 C4 9 3 6 5 3 Z" fill="none" stroke="#fff" stroke-width="1.5"/><path d="M7 11 L8 21 L11 16 L14 21 L15 11" fill="none" stroke="#fff" stroke-width="1.5"/></svg>
        Crown and<br>Bridge
      </div>
    </section>

    <p class="terms">Opening special offers valid until June 15, 2017 by Appointment only</p>
    <p class="welcome">NEW PATIENTS ARE WELCOME!</p>

    <svg class="hours-band" viewBox="0 0 604 46" aria-hidden="true">
      <path d="M0 16 H290 L302 2 L314 16 H604 V46 H0 Z" fill="#174f96"/>
    </svg>
    <p class="hours-text">Convenient Evening &amp; Saturday Hours</p>
  </article>
</div>
</body>
</html>
```